Flyer für Schulungen für Unternehmen
Zielgruppe
Wir machen Schulungen für Unternehmen zum Thema Logistik, Arbeitsmittelprüfung und Betriebssicherheit.
Aufgabenstellung
Wir haben eine neue Förderung erhalten für unsere Weiterbildung nach dem BKrFQG.
Wir können nun Schulungen ab 40€ abieten und wollen dafür Werbung gestalten. Wir möchten einen Fyler nur zum Thema Schulungen bei der Wendt Academy.

```html
<!DOCTYPE html>
<html lang="de">
<head>
<meta charset="utf-8">
<title>Wendt Academy – Schulungen</title>
<link href="https://fonts.googleapis.com/css2?family=Jost:wght@400;500;700&display=swap" rel="stylesheet">
<style>
  :root{
    --dark:#333333;
    --light:#ececec;
    --white:#ffffff;
    --green:#6cbf45;
    --band:#7a7a7a;
    --ink:#222222;
  }
  *{margin:0;padding:0;box-sizing:border-box}
  html,body{width:793px;height:1200px;overflow:hidden;background:var(--white)}
  body{font-family:'Jost',sans-serif;color:var(--ink);font-size:8.2px;line-height:11.3px}
  .flyer{position:relative;width:793px;height:1200px;overflow:hidden}
  .panel{position:absolute}
  .dark{background:var(--dark);color:var(--white)}
  .light{background:var(--light)}
  .white{background:var(--white)}
  .abs{position:absolute}
  .num{position:absolute;font-weight:700;font-size:36px;line-height:36px;letter-spacing:-1px}
  .title{position:absolute;font-weight:500;font-size:10.5px;line-height:14.5px;white-space:nowrap}
  .rule{position:absolute;height:0;border-top:.8px solid currentColor}
  .price{position:absolute;font-size:8.2px;white-space:nowrap}
  .body{position:absolute;white-space:nowrap}
  .body b{font-weight:500}
  .list div{padding-left:8px;text-indent:-8px}
  .mod{font-size:9.5px;font-weight:500}
  .photo{position:absolute}
  .brand{position:absolute;left:529px;width:264px;top:172px;text-align:center;font-weight:500;font-size:22px;line-height:26px;color:var(--ink);letter-spacing:.5px}
  .tagline{position:absolute;left:529px;width:264px;top:241px;text-align:center;font-size:8.2px;line-height:11.3px}
  .promo-head{position:absolute;left:529px;width:264px;top:305px;text-align:center;font-weight:500;font-size:9.8px;line-height:13.5px}
  .green-box{position:absolute;background:var(--green);color:var(--white)}
  .frame{position:absolute;border:.8px solid var(--ink)}
  .badge{position:absolute;background:var(--white);border:.8px solid var(--ink)}
  .contact{position:absolute;left:529px;width:264px;top:512px;color:var(--white);font-size:8.2px;line-height:12.8px}
  .contact div{display:flex;align-items:center;justify-content:center;gap:6px}
  .note{position:absolute;left:283px;top:1018px;width:227px;height:40px;background:var(--dark);color:var(--white);padding:7px 14px;white-space:nowrap}
</style>
</head>
<body>
<div class="flyer">

  <!-- 7 -->
  <section class="panel white" style="left:0;top:0;width:264px;height:235px">
    <div class="num" style="left:20px;top:14px">7</div>
    <div class="title" style="left:50px;top:24px">Sicherer Umgang mit Flurförderzeugen</div>
    <div class="rule" style="left:0;width:264px;top:43px"></div>
    <div class="price" style="left:51px;top:50px">effektiv ab 69€ netto p. P.*</div>
    <div class="rule" style="left:0;width:150px;top:61px"></div>
    <div class="body" style="left:32px;top:71px">
      Gabelstaplerschein<br><b>Dauer:</b> 8 bis 16 Stunden – Theorie und Praxis
      <div class="list" style="padding-left:16px">
        <b>Theoretischer Teil:</b>
        <div>- Erklärung der Vorschriften der Berufsgenossen<br>schaft beim Einsatz von Flurförderzeugen</div>
        <div>- Unfallverhütungsvorschrift</div>
        <div>- Kontrolle bei Arbeitsbeginn</div>
        <div>- Schriftliche Prüfung</div>
        <b>Praktischer Teil:</b>
        <div>- Tägliche Sicht- und Funktionsprüfung<br>vor Fahrtantritt</div>
        <div>- Fahrübungen</div>
        <div>- Durchführung eines Arbeitsspieles</div>
        <div>- Praktische Prüfung im Parcours</div>
      </div>
    </div>
  </section>

  <!-- 9 -->
  <section class="panel dark" style="left:264px;top:0;width:265px;height:235px">
    <div class="title" style="left:29px;top:23px">Unterweisung Ladungssicherung</div>
    <div class="num" style="left:230px;top:13px">9</div>
    <div class="rule" style="left:0;width:246px;top:43px"></div>
    <div class="price" style="left:32px;top:49px">effektiv ab 69€ netto p. P.*</div>
    <div class="rule" style="left:0;width:131px;top:61px"></div>
    <div class="body" style="left:29px;top:73px">
      <b>Dauer:</b> 8 Stunden – Theorie<br>
      Ordnungsgemäße Ladungssicherung führt zur Reduz-<br>ierung von Transportschäden, Reduzierung von Unfall-<br>und Folgekosten, sowie Vermeidung von Bußgeldern.
      <div class="list" style="padding-left:15px">
        <div>- Rechtliche Grundlagen</div>
        <div>- Verordnung sowie Richtlinien zur Ladungssicherung</div>
        <div>- Physikalische Grundlagen</div>
        <div>- Ladungssicherung bei Fahrzeugen<br>mit offener Ladefläche</div>
        <div>- Ladungssicherung bei Handwerker-<br>und Werkstattfahrzeugen</div>
        <div>- Ladungssicherung bei Fahrzeugen<br>mit Kastenaufbau</div>
      </div>
    </div>
  </section>

  <!-- 8 -->
  <section class="panel dark" style="left:0;top:235px;width:264px;height:231px">
    <div class="title" style="left:34px;top:14px">Sicherer Umgang mit Kranen</div>
    <div class="num" style="left:222px;top:3px">8</div>
    <div class="rule" style="left:0;width:245px;top:32px"></div>
    <div class="body" style="left:34px;top:41px">
      Kranschein - alle Flur &amp; Kanzelgesteuerte Krane,<br>Hallen- und Portalkrane<br>
      <b>Dauer:</b> 8-16 Stunden – Theorie und Praxis
      <div class="list" style="padding-left:16px">
        <div>- Gesetzliche Vorschriften und Vorgaben<br>der Berufsgenossenschaft</div>
        <div>- Unfallverhütungsvorschriften,<br>Bedienungsvorschriften</div>
        <div>- Sicherheitsregeln, persönliche Schutzausrüstungen</div>
        <div>- Umgang mit Lasten, Arbeit mit Traglasttabellen</div>
        <div>- Einweisung / Handzeichengebung</div>
        <div>- Anforderungen an die Kranabnahme und -prüfung</div>
        <div>- Pflege und Wartung, Sichtkontrollen<br>und Funktionsproben</div>
        <div>- Verhalten bei Störungen</div>
        <div>- Praktische Übungen</div>
        <div>- Theorieprüfung und praktischer Einzeltest</div>
      </div>
    </div>
  </section>

  <!-- 10 -->
  <section class="panel white" style="left:264px;top:235px;width:265px;height:129px">
    <div class="num" style="left:19px;top:15px">10</div>
    <div class="title" style="left:85px;top:13px">Jährliche Unterweisung<br>Flurförderzeug</div>
    <div class="rule" style="left:66px;width:199px;top:45px"></div>
    <div class="body" style="left:29px;top:53px">
      <b>Dauer:</b> 4-8 Stunden – Theorie
      <div class="list" style="padding-left:15px">
        <div>- Erklärung der Vorschriften der Berufsgenossen-<br>schaft beim Einsatz von Flurförderzeugen</div>
        <div>- Techniken von Flurförderzeugen allgemein</div>
        <div>- Unfallverhütungsvorschrift</div>
      </div>
    </div>
  </section>

  <!-- 11 -->
  <section class="panel light" style="left:264px;top:364px;width:265px;height:102px">
    <div class="title" style="left:29px;top:18px">Jährliche Unterweisung Kran</div>
    <div class="num" style="left:221px;top:6px">11</div>
    <div class="rule" style="left:0;width:246px;top:36px"></div>
    <div class="body" style="left:29px;top:48px">
      Unterweisung Kran - alle Flur &amp; kanzelgesteuerte Krane,<br>Hallen- und Portalkrane<br><b>Dauer:</b> 4-8 Stunden - Theorie
    </div>
  </section>

  <!-- 12 -->
  <section class="panel white" style="left:0;top:466px;width:529px;height:94px">
    <div class="num" style="left:35px;top:22px">12</div>
    <div class="title" style="left:87px;top:20px">Prüfungen von Arbeitsmitteln nach BetrSichV /<br>wiederkehrende Sicht- und Funktionsprüfungen nach DGUV</div>
    <div class="rule" style="left:70px;width:459px;top:52px"></div>
    <div class="body" style="left:33px;top:64px">- Herstellerunabhängige Prüfung von Leitern und Tritten</div>
    <div class="body" style="left:279px;top:64px">- Herstellerunabhängige Regalinspektion und Regalprüfung</div>
  </section>

  <!-- right column top -->
  <div class="photo" role="img" aria-label="Foto: zwei Schulungsteilnehmer in Warnweste und Schutzhelm am Gabelstapler" style="left:529px;top:0;width:264px;height:134px;background:linear-gradient(135deg,#3d4650 0%,#7a6a55 45%,#d9772e 70%,#5a6470 100%)"></div>
  <div class="panel white" style="left:529px;top:134px;width:264px;height:155px"></div>
  <div class="brand">Wendt Academy</div>
  <div class="tagline">Ihr Experte für Seminare und Schulungen rund um<br>die <b style="font-weight:500">Logistik</b> und <b style="font-weight:500">Arbeitsmittelprüfungen</b><br>nach Betriebssicherheitsverordnung</div>

  <div class="panel light" style="left:529px;top:289px;width:264px;height:192px"></div>
  <div class="promo-head">Sichern Sie sich jetzt mit unseren Fachkursen in<br>Dunningen die ESF-Förderung mit einem Zuschuss<br>von bis zu 70%!</div>

  <div class="panel dark" style="left:529px;top:481px;width:264px;height:79px"></div>

  <div class="green-box" style="left:543px;top:355px;width:126px;height:99px">
    <div class="abs" style="left:0;width:126px;top:22px;text-align:center;font-size:7px;line-height:11px;padding-left:20px">mit einem Zuschuss<br>von bis zu</div>
    <div class="abs" style="left:55px;top:46px;font-size:24px;line-height:26px;font-weight:500">70%</div>
  </div>
  <div class="frame" style="left:534px;top:366px;width:120px;height:98px"></div>
  <div class="green-box" style="left:683px;top:367px;width:94px;height:85px">
    <div class="abs" style="left:25px;top:11px;font-size:7px">ab</div>
    <div class="abs" style="left:24px;top:25px;font-size:22px;line-height:24px;font-weight:500">40€</div>
    <div class="abs" style="left:25px;top:54px;font-size:7px">netto p. P.*</div>
  </div>
  <div class="frame" style="left:690px;top:354px;width:95px;height:98px"></div>

  <div class="badge" style="left:587px;top:439px;width:67px;height:64px">
    <svg class="abs" style="left:19px;top:9px" width="30" height="30" viewBox="0 0 30 30" aria-hidden="true"><rect x="5" y="6" width="20" height="18" fill="#d7d7d7"/></svg>
  </div>
  <div class="badge" style="left:667px;top:439px;width:75px;height:64px">
    <svg class="abs" style="left:7px;top:6px" width="40" height="30" viewBox="0 0 40 30" aria-hidden="true"><rect x="0" y="0" width="34" height="22" fill="#2c4a9a"/></svg>
    <svg class="abs" style="left:5px;top:40px" width="64" height="16" viewBox="0 0 64 16" aria-hidden="true"><rect x="0" y="0" width="64" height="6" fill="#d7d7d7"/><rect x="0" y="9" width="64" height="6" fill="#d7d7d7"/></svg>
  </div>

  <div class="contact">
    <div><svg width="9" height="9" viewBox="0 0 10 10" aria-hidden="true"><circle cx="5" cy="5" r="4.3" fill="none" stroke="#fff" stroke-width=".8"/><ellipse cx="5" cy="5" rx="2" ry="4.3" fill="none" stroke="#fff" stroke-width=".8"/><line x1=".7" y1="5" x2="9.3" y2="5" stroke="#fff" stroke-width=".8"/></svg>wendt-academy-beispiel.de/</div>
    <div><svg width="9" height="9" viewBox="0 0 10 10" aria-hidden="true"><path d="M2 1 L4 1 L4.8 3.2 L3.6 4.2 Q4.6 6.2 6 6.6 L7 5.4 L9 6.2 L9 8.2 Q9 9 8 9 Q1 8.6 1 2 Q1 1 2 1Z" fill="#fff"/></svg>01234 - 5678 - 90</div>
    <div><svg width="10" height="8" viewBox="0 0 10 8" aria-hidden="true"><rect x=".5" y=".5" width="9" height="7" fill="none" stroke="#fff" stroke-width=".8"/><path d="M.5 .5 L5 4.5 L9.5 .5" fill="none" stroke="#fff" stroke-width=".8"/></svg>lena.berg@wendt-academy-beispiel.de</div>
  </div>

  <!-- band -->
  <div class="panel" style="left:0;top:560px;width:793px;height:80px;background:var(--band)"></div>

  <!-- 1 -->
  <section class="panel dark" style="left:0;top:640px;width:264px;height:211px">
    <div class="num" style="left:16px;top:20px">1</div>
    <div class="title" style="left:39px;top:32px">Eco Training und Assistenzsysteme</div>
    <div class="rule" style="left:30px;width:234px;top:49px"></div>
    <div class="price" style="left:129px;top:56px">effektiv ab 40€ netto p. P.*</div>
    <div class="rule" style="left:120px;width:144px;top:67px"></div>
    <div class="body" style="left:32px;top:80px">
      <span class="mod">Modul 1</span> nach dem BKrFQG &nbsp;| &nbsp;<b>Dauer:</b> 8 Stunden<br>
      Weiterbildung nach dem BKrFQG für Güterverkehr<br>Klasse C/CE und Personenverkehr Klasse D/DE<br>Durch das Seminar optimieren die Fahrer-/innen<br>Ihren Fahrstil zur Reduzierung des Kraftstoffver-<br>brauchs. Zusätzlich mindern die Fahrer/-innen durch<br>das Eco Training den Verschleiß am Fahrzeug. Sie<br>erwerben die notwendigen Kenntnisse für ökono-<br>misches Fahren.
    </div>
  </section>

  <!-- 2 -->
  <section class="panel light" style="left:0;top:851px;width:264px;height:221px">
    <div class="title" style="left:34px;top:24px">Sozialvorschriften und<br>Fahrtenschreiber</div>
    <div class="num" style="left:222px;top:18px">2</div>
    <div class="rule" style="left:0;width:245px;top:56px"></div>
    <div class="price" style="left:34px;top:61px">effektiv ab 40€ netto p. P.*</div>
    <div class="rule" style="left:0;width:134px;top:73px"></div>
    <div class="body" style="left:34px;top:86px">
      <span class="mod">Modul 2</span> nach dem BKrFQG &nbsp;| &nbsp;<b>Dauer:</b> 8 Stunden<br>
      Berufskraftfahrer Weiterbildung für Güterverkehr<br>Klasse C/CE und Personenverkehr Klasse D/DE<br><br>
      Seminarinhalte sind die allgemeinen Vorschriften<br>für den gewerblichen Güterverkehr, Vorschriften<br>zu Lenk- und Ruhezeiten, sowie das Auffrischen von<br>Verkehrsregeln. Um rechtlich auf dem aktuellen<br>Stand zu sein und Gefahren zu senken, sind diese<br>Kenntnisse Voraussetzung.
    </div>
  </section>

  <div class="photo" role="img" aria-label="Foto: grüner Lastwagen mit bedruckter Plane auf der Straße" style="left:0;top:1072px;width:264px;height:128px;background:linear-gradient(160deg,#6f7d6a 0%,#8a9a78 35%,#2f8a3c 60%,#5f6a60 100%)"></div>

  <!-- 3 & 4 -->
  <section class="panel white" style="left:264px;top:640px;width:265px;height:432px">
    <div class="num" style="left:19px;top:20px">3</div>
    <div class="title" style="left:121px;top:32px">Gefahrenwahrnehmung</div>
    <div class="rule" style="left:105px;width:160px;top:49px"></div>
    <div class="price" style="left:133px;top:56px">effektiv ab 40€ netto p. P.*</div>
    <div class="rule" style="left:126px;width:139px;top:67px"></div>
    <div class="body" style="left:34px;top:80px">
      <span class="mod">Modul 3</span> nach dem BKrFQG &nbsp;| &nbsp;<b>Dauer:</b> 8 Stunden<br>
      Berufskraftfahrer Weiterbildung für Güterverkehr<br>Klasse C/CE und Personenverkehr Klasse D/DE<br><br>
      Die Fahrer-/innen erweitern Ihre Kenntnisse hinsicht-<br>lich neuer Sicherheitstechniken an den Fahrzeugen.<br>Sie lernen, diese richtig zu bedienen und einzusetzen.<br>Themenschwerpunkt ist das Kennenlernen moderner
    </div>

    <div class="title" style="left:34px;top:192px">Schadensprävention</div>
    <div class="num" style="left:219px;top:180px">4</div>
    <div class="rule" style="left:0;width:246px;top:211px"></div>
    <div class="price" style="left:34px;top:216px">effektiv ab 40€ netto p. P.*</div>
    <div class="rule" style="left:0;width:133px;top:228px"></div>
    <div class="body" style="left:34px;top:240px">
      <span class="mod">Modul 4</span> nach dem BKrFQG &nbsp;| &nbsp;<b>Dauer:</b> 8 Stunden<br>
      Berufskraftfahrer Weiterbildung für Güterverkehr<br>Klasse C/CE und Personenverkehr Klasse D/DE<br><br>
      Im Seminar wird erläutert, wie Fahrer-/innen durch<br>Ihr Verhalten aktiv dazu beitragen können, ein<br>positives Firmenimage aufzubauen. Weitere Themen<br>sind: Gesundheit und Ergometrie, Alkohol, Drogen<br>und Medikamente am Steuer, richtiges Verhalten im<br>Notfall und in Notsituationen sowie Kriminalität und<br>Schleusung illegaler Einwanderer.
    </div>
  </section>
  <div class="note">*&nbsp;&nbsp;&nbsp;&nbsp; bis zu 70% Kostenersparnis durch ESF-Förderung,<br>kofinanziert von der Europäischen Union</div>

  <!-- 6 -->
  <div class="photo" role="img" aria-label="Foto: zwei Mitarbeiter in Warnweste mit Klemmbrett im Hochregallager" style="left:529px;top:640px;width:264px;height:138px;background:linear-gradient(120deg,#2f4f8a 0%,#8a5a3a 40%,#c8d24a 60%,#3a5a8a 100%)"></div>
  <section class="panel dark" style="left:529px;top:778px;width:264px;height:294px">
    <div class="num" style="left:19px;top:6px">6</div>
    <div class="title" style="left:101px;top:17px">Ausbildung Ladungssicherung</div>
    <div class="rule" style="left:31px;width:233px;top:37px"></div>
    <div class="price" style="left:136px;top:44px">effektiv ab 102€ netto p. P. *</div>
    <div class="rule" style="left:126px;width:138px;top:57px"></div>
    <div class="body" style="left:28px;top:68px">
      Ausbildung Ladungssicherung für alle am Transport<br>beteiligten Personengruppen nach VDI 2700a &nbsp;&nbsp;|<br>
      <b>Dauer:</b> 16 Stunden - Theorie und Praxis<br>
      Ordnungsgemäße Ladungssicherung führt zur Reduz-<br>ierung von Transportschäden, Reduzierung von Unfall-<br>und Folgekosten, sowie Vermeidung von Bußgeldern.
      <div class="list" style="padding-left:15px">
        <div>- Rechtliche Grundlagen</div>
        <div>- Verordnung sowie Richtlinien zur Ladungssicherung</div>
        <div>- Physikalische Grundlagen</div>
        <div>- Ladungssicherung bei Fahrzeugen<br>mit offener Ladefläche</div>
        <div>- Ladungssicherung bei Handwerker-<br>und Werkstattfahrzeugen</div>
        <div>- Ladungssicherung bei Fahrzeugen<br>mit Kastenaufbau</div>
        <div>- Ladungssicherung im Kurier-,<br>Express-, Paketdienst</div>
        <div>- Tipps und Irrtümer der Ladungssicherung</div>
        <div>- Praxisanwendungen der Sicherungs-<br>und Hilfsmittel für Transporter</div>
      </div>
    </div>
  </section>

  <!-- 5 -->
  <section class="panel light" style="left:264px;top:1072px;width:529px;height:128px">
    <div class="num" style="left:21px;top:22px">5</div>
    <div class="title" style="left:130px;top:34px">Ladungssicherung für Ladung und Fahrgast</div>
    <div class="rule" style="left:36px;width:360px;top:52px"></div>
    <div class="price" style="left:394px;top:32px">effektiv ab 40€ netto p. P.*</div>
    <div class="rule" style="left:386px;width:143px;top:43px"></div>
    <div class="body" style="left:34px;top:66px">
      <span class="mod">Modul 5</span> nach dem BKrFQG &nbsp;| &nbsp;<b>Dauer:</b> 8 Stunden<br>
      Berufskraftfahrer Weiterbildung für Güterverkehr Klasse<br>C/CE und Personenverkehr Klasse D/DE
    </div>
    <div class="body" style="left:286px;top:64px">
      In diesem Seminar vertiefen die Fahrer-/innen ihre<br>Kenntnisse zu Sicherheitsvorschriften und physikalischen<br>Gesetzen. Sie lernen, Ihre Ladung unter Anwendung von<br>Zurrmitteln und Zurrtechniken richtig zu verladen.
    </div>
  </section>

</div>
</body>
</html>
```